Pelton|Marsh & Quillan business card contest

We need a logo for an upscale boutique diversified company involved in real estate, investments, cattle, and more. Our businesses DO NOT need to be reflected in the business card nor do we want them noted. This is our logo and colors and we love our logo and colors. Our logo looks best against a black background and we like to include the firm name in our logo usage. importantly, the names Pelton and Marsh are separated by | not / and we use an ampersand not the word and.
On the front of the card, we want to include:
company logo and name (Pelton|Marsh & Quillan)
on the back, we would definitely include:
address, email, cell #
logo and name (smaller size than front)

The variable will be location of individual name and title (mine for example is ) - whether on the front OR on the back. interested in variations from which to choose
Dr. Neil R. Whitcombe, CFA
Scientifique des Fusées Financières

we would like to use contemporary symbols for address, email address, cell # with an option for web site that we do not intend to use initially. we like two sided cards and believe this design should use four rounded corners with the standard size. we prefer thicker card stock and may look at metal.

```html
<!DOCTYPE html>
<html lang="en">
<head>
<meta charset="UTF-8">
<title>Pelton|Marsh &amp; Quillan — Business Card</title>
<link href="https://fonts.googleapis.com/css2?family=Lato:wght@400;700&display=swap" rel="stylesheet">
<style>
  :root {
    --page-bg: #e6e6e6;
    --card-black: #000000;
    --orange-top: #e8842a;
    --orange-bottom: #c9532b;
    --orange-text: #cf5e2a;
    --stripe-grey: #5a5a5a;
    --brand-grey: #6e6e6e;
    --text-grey: #a3a3a3;
  }
  * { margin: 0; padding: 0; box-sizing: border-box; }
  html, body {
    width: 1200px; height: 1200px; overflow: hidden;
    background: var(--page-bg);
    font-family: "Lato", sans-serif;
  }
  .canvas { position: relative; width: 1200px; height: 1200px; }

  .card {
    position: absolute;
    left: 296px;
    width: 608px; height: 348px;
    background: var(--card-black);
    border-radius: 28px;
    overflow: hidden;
  }
  .card--front { top: 221px; }
  .card--back { top: 631px; }

  .edge-band {
    position: absolute; left: 0; top: 0; bottom: 0; width: 22px;
    background: linear-gradient(to bottom, var(--orange-top), var(--orange-bottom));
  }
  .edge-rule {
    position: absolute; left: 22px; top: 0; bottom: 0; width: 8px;
    background: var(--stripe-grey);
  }

  .brand {
    position: absolute;
    display: flex; align-items: center; gap: 8px;
    color: var(--brand-grey);
    font-weight: 400;
    white-space: nowrap;
  }
  .brand__square { background: var(--orange-top); flex: none; }
  .brand--small { left: 56px; top: 76px; font-size: 17px; letter-spacing: 0.5px; }
  .brand--small .brand__square { width: 12px; height: 12px; }
  .brand--large {
    left: 50%; top: 50%; transform: translate(-50%, -50%);
    font-size: 30px; letter-spacing: 0.8px; gap: 14px;
  }
  .brand--large .brand__square { width: 20px; height: 20px; }

  .person {
    position: absolute; right: 35px; top: 142px;
    text-align: right;
  }
  .person__name {
    color: var(--orange-text);
    font-size: 20.5px; font-weight: 700; letter-spacing: 0.1px;
    line-height: 1.15;
  }
  .person__cred { color: var(--text-grey); font-size: 13px; font-weight: 700; }
  .person__title {
    color: var(--text-grey);
    font-size: 13px; letter-spacing: 1.1px;
    margin-top: 1px;
  }
  .person-marker {
    position: absolute; left: 582px; top: 151px;
    width: 4px; height: 28px; background: var(--orange-text);
  }

  .contact {
    position: absolute; left: 56px; top: 232px;
    color: var(--text-grey);
    font-size: 13.5px; letter-spacing: 1px; line-height: 19.5px;
    list-style: none;
  }
  .contact__line { display: flex; align-items: center; }
  .contact__icon { width: 11px; height: 11px; margin: 0 12px 0 1px; flex: none; }
</style>
</head>
<body>
<main class="canvas">

  <section class="card card--front" aria-label="Business card front">
    <div class="edge-band"></div>
    <div class="edge-rule"></div>

    <div class="brand brand--small">
      <span class="brand__square"></span>
      <span class="brand__name">Pelton|Marsh &amp; Quillan</span>
    </div>

    <div class="person">
      <p class="person__name">Dr. Neil R. Whitcombe, <span class="person__cred">CFA</span></p>
      <p class="person__title">Scientifique des Fusées Financières</p>
    </div>
    <div class="person-marker"></div>

    <ul class="contact">
      <li class="contact__line">48 Harrow Lane, Suite# B</li>
      <li class="contact__line">London, UK 472B18</li>
      <li class="contact__line">
        <svg class="contact__icon" viewBox="0 0 24 24" aria-hidden="true"><path fill="#e8842a" d="M6.6 10.8a15.1 15.1 0 0 0 6.6 6.6l2.2-2.2a1 1 0 0 1 1-.25 11.4 11.4 0 0 0 3.6.57 1 1 0 0 1 1 1V20a1 1 0 0 1-1 1A17 17 0 0 1 3 4a1 1 0 0 1 1-1h3.5a1 1 0 0 1 1 1c0 1.25.2 2.45.57 3.57a1 1 0 0 1-.25 1z"/></svg>
        024 356 910
      </li>
      <li class="contact__line">
        <svg class="contact__icon" viewBox="0 0 24 24" aria-hidden="true"><rect x="2" y="5" width="20" height="14" rx="1.5" fill="none" stroke="#e8842a" stroke-width="2.4"/><path d="M3 6l9 7 9-7" fill="none" stroke="#e8842a" stroke-width="2.4"/></svg>
        office@peltonmarsh.example
      </li>
      <li class="contact__line">
        <svg class="contact__icon" viewBox="0 0 24 24" aria-hidden="true"><g fill="none" stroke="#e8842a" stroke-width="2"><circle cx="12" cy="12" r="10"/><ellipse cx="12" cy="12" rx="4.5" ry="10"/><path d="M2 12h20M4 7h16M4 17h16"/></g></svg>
        www.peltonmarsh.example
      </li>
    </ul>
  </section>

  <section class="card card--back" aria-label="Business card back">
    <div class="brand brand--large">
      <span class="brand__square"></span>
      <span class="brand__name">Pelton|Marsh &amp; Quillan</span>
    </div>
  </section>

</main>
</body>
</html>
```